Brightwell Works Capability Statement 2019

this document will be used to draw new business in so it NEEDS to be engaging and the prospective client will need to want to flip the page and read on.
this will be an engaging, ultra modern capability statement.
Pages i need created including text as per attachments capability statement 2018 REV
Fresh new Photos will need to be taken from from photo stock or similar site please do not use photos on existing attachments
Logo attached
Updates

Target Market(s)

Commercial building, facility managers, asset managers, strata markets

Industry/Entity Type

Construction Company

Colors

Designer to choose colors to be used in the design.

Requirements
Must have
• fresh, ultra modern and engaging.
• needs very fresh and crisp images, visually appealing colour scheme that draws the reader in
• - Referencing our QLD branch - covering the eastern seaboard
• - professional outfit
• - designs need to go all the way to edge of page
Nice to have
• all details in must haves
Should not have
• outdated colour scheme, outdated old - pixelated photos , not cropped in or border

```html
<!DOCTYPE html>
<html lang="en">
<head>
<meta charset="utf-8">
<title>Brightwell Works Capability Statement 2019</title>
<link rel="stylesheet" href="https://fonts.googleapis.com/css2?family=Archivo:ital,wght@0,400;0,600;0,800;1,800&display=swap">
<style>
:root{
  --orange:#f07d1a;
  --navy:#2b2f7a;
  --ink:#1c1c24;
  --paper:#ffffff;
  --stage:#e4e4e4;
  --grey:#6d6d75;
}
*{box-sizing:border-box;margin:0;padding:0}
html,body{width:1200px;height:840px;overflow:hidden;background:var(--stage)}
body{font-family:"Archivo",Arial,sans-serif;color:var(--ink);position:relative}
.page{position:absolute;top:150px;width:380px;height:537px;background:var(--paper);overflow:hidden;box-shadow:0 6px 18px rgba(0,0,0,.12)}
.page--6{left:20px}
.page--7{left:400px;box-shadow:0 6px 18px rgba(0,0,0,.12),inset 8px 0 10px -8px rgba(0,0,0,.18)}
.page--skills{left:800px}
.running-head{position:absolute;top:18px;left:22px;display:flex;align-items:center;gap:6px}
.running-head__year{background:var(--orange);color:#fff;font-weight:800;font-size:8px;padding:2px 7px}
.running-head__title{color:var(--navy);font-weight:800;font-style:italic;font-size:8px;letter-spacing:.2px}
.hero{position:absolute;top:40px;left:0;width:380px;height:150px;background:linear-gradient(135deg,#3a3530,#8a8578 55%,#d9d6cf);}
.hero__title{position:absolute;left:22px;bottom:14px;color:var(--orange);font-weight:800;font-style:italic;font-size:19px;line-height:1;text-transform:uppercase;text-shadow:0 1px 0 #000}
.column{position:absolute;font-size:7.4px;line-height:1.32}
.column h2{color:var(--orange);font-weight:800;font-style:italic;font-size:13px;margin-bottom:4px}
.column p{margin-bottom:6px}
.column ul{list-style:none}
.column li{position:relative;padding-left:9px;margin-bottom:1px}
.column li::before{content:"";position:absolute;left:0;top:2px;width:4px;height:4px;background:var(--orange)}
.col-painting{top:206px;left:22px;width:160px}
.col-waterproof{top:206px;left:198px;width:160px}
.footer-url{position:absolute;bottom:20px;right:22px;color:var(--navy);font-weight:800;font-style:italic;font-size:8px}
.folio{position:absolute;bottom:20px;font-weight:800;color:var(--navy);font-size:8px}
.page--6 .folio{left:22px}
.page--7 .folio{left:22px}
.brand{position:absolute;top:14px;right:22px;text-align:right}
.brand__name{color:var(--navy);font-weight:800;font-size:17px;line-height:1}
.brand__tag{color:var(--grey);font-size:7px;margin-top:2px}
.photo{position:absolute;left:0;width:380px}
.photo--roller{top:52px;height:100px;background:linear-gradient(160deg,#8a8c8e,#d7d8d8 60%,#5d6166)}
.photo--torch{top:152px;height:112px;background:linear-gradient(135deg,#7b5a52,#d58a4c 45%,#8f7d7d)}
.photo--tiler{top:330px;height:90px;background:linear-gradient(170deg,#2c2f3a,#b8b2a8 60%,#6c5a50)}
.photo--membrane{top:420px;height:80px;background:linear-gradient(160deg,#8a8a8e,#c9b7a8 50%,#b56a4f)}
.col-skills{top:60px;left:200px;width:158px}
.col-skills h2{font-size:12px;text-transform:uppercase}
.col-skills .lead{color:var(--navy);font-weight:600;margin-bottom:2px}
.col-tiling{top:60px;left:22px;width:165px}
.col-tiling h3{display:inline;color:var(--orange);font-weight:800;font-style:italic;font-size:11px}
.photo--house{top:330px;left:150px;width:230px;height:170px;background:linear-gradient(180deg,#cfe1ee,#eef2f4 45%,#9aa6a0 70%,#6f8a3e)}
</style>
</head>
<body>

<section class="page page--6">
  <div class="running-head"><span class="running-head__year">2019</span><span class="running-head__title">CAPABILITY STATEMENT</span></div>
  <div class="hero" role="img" aria-label="Photo of a paint roller resting on an open tin of white paint">
    <div class="hero__title">Core services and<br>capabilities</div>
  </div>
  <div class="column col-painting">
    <h2>Painting</h2>
    <p>– Award winning specialists in large-scale internal and external painting for multi-storey strata and commercial buildings, recognised for our expertise, professional finishes and painting projects for buildings with difficult access.</p>
    <ul>
      <li>Exterior strata building painting</li>
      <li>Internal strata or commercial painting</li>
      <li>Structured maintenance painting for your individual property</li>
      <li>Apartment or unit interior painting (walls, ceilings, doors and window frames)</li>
      <li>Common areas painting (foyer, laundry or garbage rooms)</li>
      <li>Difficult-access sites (such as multi-storey strata or heritage commercial buildings)</li>
    </ul>
  </div>
  <div class="column col-waterproof">
    <h2>Waterproofing</h2>
    <p>– Providing protective waterproofing for strata, commercial or residential property. Our experience in difficult-access strata and commercial waterproofing jobs over 20 years means we have the team in place to complete your waterproofing job quickly with minimum disruption to owners and tenants.</p>
    <ul>
      <li>Roof top membranes waterproofing and drainage works</li>
      <li>Balconies waterproofing and drainage works</li>
      <li>Basement works</li>
      <li>Common areas in apartment blocks or commercial buildings</li>
    </ul>
    <p style="margin-top:6px">We use only the latest technologies and products including torch-on membranes, liquid epoxy and water-based membranes, to ensure the treatment lasts longer.</p>
  </div>
  <div class="folio">6</div>
  <div class="footer-url">www.brightwellworks.com.au</div>
</section>

<section class="page page--7">
  <div class="brand">
    <div class="brand__name">Brightwell Works</div>
    <div class="brand__tag">strata painting &amp; remedial repair</div>
  </div>
  <div class="photo photo--roller" role="img" aria-label="Photo of a roller spreading waterproofing coating on a concrete surface"></div>
  <div class="photo photo--torch" role="img" aria-label="Photo of a torch-on membrane being heat sealed"></div>
  <div class="photo photo--tiler" role="img" aria-label="Photo of a tradesperson laying floor tiles"></div>
  <div class="photo photo--membrane" role="img" aria-label="Photo of liquid membrane being applied to a floor"></div>
  <div class="folio" style="bottom:20px">7</div>
</section>

<section class="page page--skills">
  <div class="running-head"><span class="running-head__year">2019</span><span class="running-head__title">CAPABILITY STATEMENT</span></div>
  <div class="brand" style="top:40px">
    <div class="brand__name">Brightwell Works</div>
    <div class="brand__tag">strata painting &amp; remedial repair</div>
  </div>
  <div class="column col-tiling" style="top:82px">
    <p><h3>Tiling</h3> – We have a reputation for outstanding tiling projects with our clients. Before we begin to lay tiles we need to know that the underlying surface is watertight and dry which is why we suggest that you use Brightwell Works for both your waterproofing and tiling needs. When it comes to tiling common areas in your strata or commercial property, we need to manage risk and liability to prevent anyone slipping on common-area tiles and injuring themselves. To mitigate this issue, we'll help you understand the slip rating on your tiles before you make your final choice. Our team know their tiles and can assure the finished job will be perfectly finished and pleasing to look at.</p>
    <p><h3>Spalling Repairs</h3> – We use only the latest technologies (including Corvia and Densil) to stop unsightly and dangerous concrete cancer and drummy cement render in strata and commercial buildings:</p>
    <ul>
      <li>Concrete floors</li>
      <li>Slab edges, beams and soffits</li>
      <li>Cement render walls</li>
      <li>Basements</li>
      <li>Ceilings</li>
    </ul>
  </div>
  <div class="column col-skills" style="top:100px">
    <h2>Competitive skills</h2>
    <p class="lead">We provide:</p>
    <ul>
      <li>Itemised written quotations with fixed lump sum contracts</li>
      <li>Large-scale commercial and strata experience</li>
      <li>Sydney-wide coverage</li>
      <li>Flexibility in rescheduling job start dates</li>
      <li>30 full-time painters and tradespeople</li>
      <li>Dedicated project manager for each job, for better co-ordination of trades</li>
      <li>High-quality jobs</li>
      <li>Robust processes to ensure your project is well managed</li>
      <li>On time and on budget</li>
      <li>Responsive and timely communication</li>
      <li>Fair and competitive pricing</li>
      <li>Harrow Paints and Kestrel Coatings accredited with volume discount, which means savings for our client</li>
    </ul>
  </div>
  <div class="photo photo--house" role="img" aria-label="Photo of a new two-storey house under construction"></div>
  <div class="footer-url">www.brightwellworks.com.au</div>
</section>

</body>
</html>
```